Wedding DJ Services Flyer

Need to make a classy flyer showing and describing different services we offer. I have actual photos from weddings we have done in the past. Stock photos are ok too. Just looking for a front and back, blank space for pricing. Need website and other company info (logo) on the flyer. Front needs to pop with a tagline that screams wedding dj and as soon as a customer sees it, they want to book us. Services we offer are DJ/Emcee, Karaoke, Uplighting, Custom Monogram Projection, Dancing on the Clouds, Custom Love Story Video Slideshow (see my photos, stock photos are ok too).Marlo Vance Entertainment Group, We have been in business since 1998 and provide DJ Event services to all of central and northeastern Pennsylvania. want social media icons on flyer (facebook,instagram,twitter) by website (www.Tqpk.org) and email (Marlo@tqpk.org), phone number 555-283-0146 (call or Text)MORE PHOTOS AVAIL BY REQUEST. Designer should have some knowledge or prior design with this type of business

Target Market(s)

brides and grooms 18-50 yoa

Industry/Entity Type

Entertainment Industry

Colors

Designer to choose colors to be used in the design.

Requirements
Must have
• Photos and descriptions of services we offer

```html
<!DOCTYPE html>
<html lang="en">
<head>
<meta charset="utf-8">
<title>Marlo Vance Entertainment Group – Wedding DJ Flyer</title>
<link rel="stylesheet" href="https://fonts.googleapis.com/css2?family=Bebas+Neue&family=Montserrat:wght@400;500;600&family=Playfair+Display:ital,wght@1,700&display=swap">
<style>
  :root{
    --purple:#a51fc8;
    --purple-deep:#4a0f6b;
    --purple-dark:#2a0a3f;
    --magenta:#c23be0;
    --grey-dark:#3e3e44;
    --grey-mid:#7c7c82;
    --grey-icon:#8d8d92;
    --paper:#f7f6f8;
    --backdrop:#e4e2e7;
  }
  *{box-sizing:border-box;margin:0;padding:0}
  html,body{width:720px;height:1200px;overflow:hidden;background:var(--backdrop)}
  body{position:relative;font-family:"Montserrat",sans-serif;color:var(--grey-dark)}

  .flyer{position:absolute;left:150px;width:420px;height:570px;background:var(--paper);overflow:hidden;box-shadow:0 4px 14px rgba(0,0,0,.18)}
  .flyer--front{top:20px}
  .flyer--back{top:610px}
  .flyer__art{position:absolute;inset:0;width:420px;height:570px}

  .brand{position:absolute;left:22px;top:22px;width:120px;font-family:"Montserrat",sans-serif;font-weight:600;font-size:11px;line-height:1.25;color:var(--grey-dark)}

  .headline{position:absolute;left:70px;top:318px;font-family:"Bebas Neue",sans-serif;line-height:.9}
  .headline__stack{display:inline-block;color:var(--purple);font-size:40px;vertical-align:bottom}
  .headline__dj{display:inline-block;color:var(--grey-dark);font-size:96px;margin-left:4px;vertical-align:bottom;line-height:.8}
  .tagline{position:absolute;left:70px;top:397px;font-family:"Playfair Display",serif;font-style:italic;font-weight:700;font-size:15px;color:var(--grey-dark)}
  .intro{position:absolute;left:40px;right:40px;top:424px;text-align:center;font-size:7.5px;line-height:1.4;color:var(--grey-dark)}

  .call-pill{position:absolute;left:110px;top:452px;width:200px;height:24px;border-radius:12px;background:var(--purple);color:#fff;font-family:"Bebas Neue",sans-serif;font-size:16px;letter-spacing:.5px;text-align:center;line-height:25px}

  .contact{position:absolute;display:flex;align-items:center;gap:6px;font-size:9px;color:var(--grey-dark)}
  .contact svg{flex:none}
  .social{position:absolute;display:flex;align-items:center;gap:5px;font-size:9px;color:var(--grey-dark)}
  .social__dot{width:10px;height:10px;border-radius:2px;background:var(--purple)}

  .book-now{position:absolute;left:58px;top:160px;width:124px;height:124px;border-radius:50%;background:var(--purple);border:4px solid var(--paper);color:#fff;font-family:"Bebas Neue",sans-serif;font-size:40px;line-height:.9;display:flex;align-items:center;justify-content:center;text-align:center}
  .services-title{position:absolute;left:160px;top:262px;padding:3px 10px;border:1.5px solid var(--grey-dark);font-weight:600;font-size:15px;letter-spacing:1px;color:var(--grey-dark);background:var(--paper)}

  .service{position:absolute;width:110px;text-align:center;font-size:8.5px;line-height:1.2;letter-spacing:.5px;text-transform:uppercase;color:var(--grey-dark)}
  .service__icon{display:block;margin:0 auto 5px;width:34px;height:34px}
</style>
</head>
<body>

<!-- FRONT -->
<section class="flyer flyer--front">
  <svg class="flyer__art" viewBox="0 0 420 570">
    <defs>
      <linearGradient id="front-sky" x1="0" y1="0" x2="0" y2="1">
        <stop offset="0" stop-color="#fbf3fa"/>
        <stop offset=".3" stop-color="#d89ee6"/>
        <stop offset=".55" stop-color="#6a1a94"/>
        <stop offset="1" stop-color="#2a0a3f"/>
      </linearGradient>
    </defs>
    <path d="M0 300 Q220 300 420 170" fill="none" stroke="var(--purple)" stroke-width="10"/>
    <g role="img" aria-label="Reception hall lit with purple uplighting">
      <path d="M0 0 H420 V165 Q220 295 0 295 Z" fill="url(#front-sky)"/>
    </g>
    <path d="M0 80 Q200 60 420 60" fill="none" stroke="var(--purple)" stroke-width="3" opacity=".7"/>
    <g role="img" aria-label="Bride dancing at a reception">
      <circle cx="95" cy="170" r="55" fill="#8d6f86" stroke="#fff" stroke-width="3"/>
    </g>
    <g role="img" aria-label="Bride and groom outdoors on the lawn">
      <circle cx="330" cy="120" r="55" fill="#c9b8c7" stroke="#fff" stroke-width="3"/>
    </g>
    <g role="img" aria-label="Newlyweds posing together at the venue">
      <circle cx="210" cy="160" r="70" fill="#7f8a5d" stroke="#fff" stroke-width="3"/>
    </g>
  </svg>

  <div class="brand">Marlo Vance<br>Entertainment<br>Group</div>

  <h1 class="headline">
    <span class="headline__stack">Screams<br>Wedding</span><span class="headline__dj">DJ</span>
  </h1>
  <p class="tagline">and as soon as a customer sees it</p>
  <p class="intro">We have been in business since 1998 and provide DJ Event services to all of central and northeastern Pennsylvania.</p>

  <div class="call-pill">Call us or text : 555-283-0146</div>

  <div class="contact" style="left:110px;top:490px">
    <svg width="12" height="9" viewBox="0 0 12 9"><rect x=".5" y=".5" width="11" height="8" fill="none" stroke="var(--purple)"/><path d="M.5 .5 L6 5 L11.5 .5" fill="none" stroke="var(--purple)"/></svg>
    Marlo@tqpk.org
  </div>
  <div class="social" style="left:260px;top:490px">
    Follow US On
    <span class="social__dot"></span><span class="social__dot"></span><span class="social__dot"></span>
  </div>
  <div class="contact" style="left:110px;top:525px">
    <svg width="10" height="10" viewBox="0 0 10 10"><circle cx="5" cy="5" r="4.5" fill="var(--purple)"/><path d="M.5 5 H9.5 M5 .5 V9.5" stroke="#fff" stroke-width=".8"/></svg>
    www.Tqpk.org
  </div>
</section>

<!-- BACK -->
<section class="flyer flyer--back">
  <svg class="flyer__art" viewBox="0 0 420 570">
    <defs>
      <linearGradient id="back-hall" x1="0" y1="0" x2="0" y2="1">
        <stop offset="0" stop-color="#7a2ac9"/>
        <stop offset=".5" stop-color="#5a1499"/>
        <stop offset="1" stop-color="#2a0a3f"/>
      </linearGradient>
    </defs>
    <path d="M0 262 Q200 200 420 200" fill="none" stroke="var(--purple)" stroke-width="10"/>
    <g role="img" aria-label="DJ setup with purple lighting and a projected couple monogram">
      <path d="M0 0 H420 V196 Q200 196 0 258 Z" fill="url(#back-hall)"/>
    </g>
  </svg>

  <div class="book-now">Book<br>Now</div>
  <h2 class="services-title">SERVICES</h2>

  <div class="service" style="left:30px;top:335px">
    <svg class="service__icon" viewBox="0 0 34 34"><circle cx="17" cy="17" r="17" fill="var(--grey-icon)"/><rect x="9" y="18" width="16" height="7" fill="#fff"/><rect x="15" y="9" width="4" height="9" fill="#fff"/></svg>
    DJ/Emcee
  </div>
  <div class="service" style="left:160px;top:300px">
    <svg class="service__icon" viewBox="0 0 34 34"><circle cx="17" cy="17" r="17" fill="var(--grey-icon)"/><circle cx="19" cy="13" r="5" fill="#fff"/><path d="M15 17 L9 25" stroke="#fff" stroke-width="3" stroke-linecap="round"/></svg>
    Karaoke
  </div>
  <div class="service" style="left:280px;top:270px">
    <svg class="service__icon" viewBox="0 0 34 34"><circle cx="17" cy="17" r="17" fill="var(--grey-icon)"/><path d="M9 21 a4 4 0 0 1 2-7 a6 6 0 0 1 11-1 a4 4 0 0 1 3 8 Z" fill="#fff"/></svg>
    Dancing on<br>the clouds
  </div>
  <div class="service" style="left:45px;top:410px">
    <svg class="service__icon" viewBox="0 0 34 34"><circle cx="17" cy="17" r="17" fill="var(--grey-icon)"/><circle cx="17" cy="15" r="6" fill="#fff"/><rect x="14" y="21" width="6" height="4" fill="#fff"/><path d="M6 15 H9 M25 15 H28 M17 4 V7" stroke="#fff" stroke-width="2"/></svg>
    Uplighting
  </div>
  <div class="service" style="left:165px;top:375px">
    <svg class="service__icon" viewBox="0 0 34 34"><circle cx="17" cy="17" r="17" fill="var(--grey-icon)"/><circle cx="17" cy="17" r="9" fill="none" stroke="#fff" stroke-width="2"/><circle cx="17" cy="17" r="4" fill="none" stroke="#fff" stroke-width="2"/></svg>
    Custom<br>monogram<br>projection
  </div>
  <div class="service" style="left:280px;top:335px">
    <svg class="service__icon" viewBox="0 0 34 34"><circle cx="17" cy="17" r="17" fill="var(--grey-icon)"/><rect x="8" y="10" width="18" height="14" rx="2" fill="none" stroke="#fff" stroke-width="2"/><path d="M15 13 L21 17 L15 21 Z" fill="#fff"/></svg>
    Custom<br>love story<br>video<br>slideshow
  </div>

  <div class="social" style="left:270px;top:440px">
    Follow US On
    <span class="social__dot"></span><span class="social__dot"></span><span class="social__dot"></span>
  </div>
  <div class="contact" style="left:215px;top:490px">
    <svg width="12" height="9" viewBox="0 0 12 9"><rect x=".5" y=".5" width="11" height="8" fill="none" stroke="var(--purple)"/><path d="M.5 .5 L6 5 L11.5 .5" fill="none" stroke="var(--purple)"/></svg>
    Marlo@tqpk.org
  </div>
  <div class="contact" style="left:70px;top:510px">
    <svg width="10" height="10" viewBox="0 0 10 10"><circle cx="5" cy="5" r="4.5" fill="var(--purple)"/><path d="M.5 5 H9.5 M5 .5 V9.5" stroke="#fff" stroke-width=".8"/></svg>
    www.Tqpk.org
  </div>
</section>

</body>
</html>
```